Bottle label for a drinking or cocktail vinegar called Stone Hollow Shrub

We need a label for a square bottle that measures 2.75 inches on a side and is 6.75 inches tall. The volume is 16.9oz/500mL. The corners are rounded. A photo has been uploaded. The label should be one piece that wraps around 2-3 sides rather than separate front and back labels. The maximum height of the label can be 3.25 inches.

The company name is Stone Hollow Vinegar Works. The product line is called Stone Hollow Shrub.

The product is what is called a drinking vinegar, or sometimes cocktail vinegar, the kind of vinegar that is added to cocktails or used to make a beverage. Drinking vinegar, also known as a shrub, is vinegar and sugar mixed with fruit. The resulting elixir is tart and sweet, and is used as an alternative to lemon or lime in many drinks where it introduces an acid but with a different fruit flavor. A simple, non-alcoholic beverage can be made by adding shrub to sparkling water over ice.

Stone Hollow Shrubs are handcrafted in small batches in a small town called Deep River which is on the bank of the Connecticut River in New England. Some of the flavors include Pomegranate, Pineapple/Basil, Cherry, Fennel/Apple, and Elderberry. New flavors are added and old flavors go away, such is the nature of small batch production.

Some key words that may be useful are: artisan, small batch, handcrafted, cocktail vinegar, drinking vinegar, shrub, seasonal, natural, whole fruit.

Target Market(s)

The target audience is 25-40 year olds that drink cocktails rather than beer.

Requirements
Must have
• In addition to usual label contents (name, ingredients, volume, company info, etc.), There should be space for a hand written Batch number, description of a shrub, sample recipes, “Shake before using”.
Should not have
• nutrition labeling is not needed

```html
<!DOCTYPE html>
<html lang="en">
<head>
<meta charset="utf-8">
<title>Stone Hollow Shrub – Label Range</title>
<link href="https://fonts.googleapis.com/css2?family=Oswald:wght@400;500;700&family=Lobster+Two:wght@700&display=swap" rel="stylesheet">
<style>
  :root {
    --page: #ffffff;
    --label: #fbe8cd;
    --ink: #231f20;
    --pineapple: #f1b31c;
    --pineapple-text: #4e8a2b;
    --fennel: #7da638;
    --fennel-text: #d3262e;
    --pomegranate: #c21f30;
    --pomegranate-text: #fbe8cd;
  }
  * { box-sizing: border-box; margin: 0; padding: 0; }
  html, body {
    width: 1200px;
    height: 1070px;
    overflow: hidden;
    background: var(--page);
  }
  .label-range {
    width: 1200px;
    height: 1070px;
    display: flex;
    justify-content: center;
    align-items: center;
    gap: 30px;
  }
  .label {
    position: relative;
    width: 360px;
    height: 540px;
    background: var(--label);
    color: var(--ink);
    font-family: "Oswald", sans-serif;
    padding: 40px 34px 26px;
    display: flex;
    flex-direction: column;
    align-items: center;
  }
  .maker {
    display: flex;
    align-items: center;
    gap: 10px;
    align-self: center;
  }
  .maker-mark {
    width: 16px;
    height: 16px;
    background: var(--ink);
  }
  .maker-name {
    font-weight: 500;
    font-size: 21px;
    letter-spacing: 0.5px;
    line-height: 1;
    text-transform: uppercase;
  }
  .product-name {
    margin-top: 38px;
    text-align: center;
    line-height: 0.95;
    text-transform: uppercase;
  }
  .product-line {
    display: block;
    font-weight: 400;
    font-size: 50px;
    letter-spacing: -0.5px;
  }
  .product-type {
    display: block;
    font-weight: 700;
    font-size: 104px;
    letter-spacing: -1px;
  }
  .flavor-ribbon {
    margin-top: 12px;
    width: 270px;
    height: 40px;
    display: flex;
    align-items: center;
    justify-content: center;
    font-family: "Lobster Two", cursive;
    font-weight: 700;
    font-size: 24px;
    letter-spacing: 0.5px;
    clip-path: polygon(0 0, 100% 0, 96% 50%, 100% 100%, 0 100%, 4% 50%);
  }
  .flavor-pineapple .flavor-ribbon { background: var(--pineapple); color: var(--pineapple-text); }
  .flavor-fennel .flavor-ribbon { background: var(--fennel); color: var(--fennel-text); }
  .flavor-pomegranate .flavor-ribbon { background: var(--pomegranate); color: var(--pomegranate-text); }
  .cocktail-art {
    margin-top: 18px;
    width: 292px;
    height: 150px;
  }
  .flavor-pineapple .cocktail-art { background: linear-gradient(180deg, #f4dcaf 0%, #f2c25e 100%); }
  .flavor-fennel .cocktail-art { background: linear-gradient(180deg, #eadfb8 0%, #a9c16d 100%); }
  .flavor-pomegranate .cocktail-art { background: linear-gradient(180deg, #f0d1bd 0%, #d05a5d 100%); }
  .volume {
    margin-top: auto;
    width: 100%;
    display: flex;
    justify-content: space-between;
    font-weight: 400;
    font-size: 19px;
    letter-spacing: 0.3px;
  }
</style>
</head>
<body>
<main class="label-range">

  <article class="label flavor-pineapple">
    <div class="maker"><span class="maker-mark"></span><span class="maker-name">Stone Hollow Vinegar Works</span></div>
    <h1 class="product-name"><span class="product-line">Stone Hollow</span><span class="product-type">Shrub</span></h1>
    <div class="flavor-ribbon">Pineapple/Basil</div>
    <div class="cocktail-art" role="img" aria-label="Sketched martini glass with yellow pineapple-basil shrub and a green olive on a pick"></div>
    <div class="volume"><span>16.9OZ</span><span>500ML</span></div>
  </article>

  <article class="label flavor-fennel">
    <div class="maker"><span class="maker-mark"></span><span class="maker-name">Stone Hollow Vinegar Works</span></div>
    <h1 class="product-name"><span class="product-line">Stone Hollow</span><span class="product-type">Shrub</span></h1>
    <div class="flavor-ribbon">Fennel/Apple</div>
    <div class="cocktail-art" role="img" aria-label="Sketched martini glass with green fennel-apple shrub and a green olive on a pick"></div>
    <div class="volume"><span>16.9OZ</span><span>500ML</span></div>
  </article>

  <article class="label flavor-pomegranate">
    <div class="maker"><span class="maker-mark"></span><span class="maker-name">Stone Hollow Vinegar Works</span></div>
    <h1 class="product-name"><span class="product-line">Stone Hollow</span><span class="product-type">Shrub</span></h1>
    <div class="flavor-ribbon">Pomegranate</div>
    <div class="cocktail-art" role="img" aria-label="Sketched martini glass with red pomegranate shrub and a black olive on a pick"></div>
    <div class="volume"><span>16.9OZ</span><span>500ML</span></div>
  </article>

</main>
</body>
</html>
```